Architecture firm needing a business card

We need a business card design for a new company based in the US called "Pellmore Architecture". Seeking minimalist designs that have a creativity/design feel but must be clean and professional. Please refer to the logo attached.

Target Market(s)

Real Estate Investors, Home Builders and Construction Firms.

Industry/Entity Type

Architecture

Contact Information for Business Card

Standard US size business cards. Would like to have some sort of graphic on the back side of the card - nothing that is too loud but something that may catch your attention. More or less grayscale colors that are in line with the logo colors (navy and greys essentially). Additional colors maybe accepted if blended properly (earthtones), but might be difficult to accomplish and maintain the clean/minimalist look.

Requirements
Must have
• Clean Lines
Nice to have
• some sort of graphics, would like to have something creative on the back side of the card
Should not have
• nothing too busy, cluttered or overwhelming.

```html
<!DOCTYPE html>
<html lang="en">
<head>
<meta charset="utf-8">
<title>Pellmore Architecture – Business Card</title>
<link href="https://fonts.googleapis.com/css2?family=Open+Sans:wght@400;600&display=swap" rel="stylesheet">
<style>
  :root {
    --stage: #a9a7a8;
    --card: #fbfbfb;
    --navy: #2b4a70;
    --grey: #9a9a9a;
    --text-grey: #555a60;
    --faint: #eef0f3;
  }
  * { margin: 0; padding: 0; box-sizing: border-box; }
  html, body { width: 1200px; height: 1200px; overflow: hidden; }
  body {
    background: var(--stage);
    font-family: "Open Sans", sans-serif;
    position: relative;
  }
  .card {
    position: absolute;
    left: 240px;
    width: 712px;
    height: 419px;
    background: var(--card);
    border-radius: 22px;
    overflow: hidden;
  }
  .card--front { top: 118px; }
  .card--back { top: 645px; }

  .faint-pattern {
    position: absolute;
    background: var(--faint);
  }
  .card--front .faint-pattern { left: 28px; top: 24px; width: 656px; height: 371px; opacity: .55; }
  .card--front .logo-clear {
    position: absolute; left: 140px; top: 140px; width: 432px; height: 130px;
    background: var(--card);
  }

  .wordmark {
    position: absolute;
    display: flex;
    align-items: center;
    color: var(--navy);
    font-weight: 400;
  }
  .wordmark__square { background: var(--navy); flex: none; }
  .wordmark__name { line-height: 1; }
  .wordmark__name span { display: block; }

  .card--front .wordmark { left: 156px; top: 162px; gap: 20px; }
  .card--front .wordmark__square { width: 80px; height: 80px; }
  .card--front .wordmark__firm { font-size: 60px; letter-spacing: 1px; }
  .card--front .wordmark__kind { font-size: 25px; letter-spacing: 6.2px; margin-top: 8px; }

  .card--back .wordmark { left: 55px; top: 76px; gap: 12px; }
  .card--back .wordmark__square { width: 50px; height: 50px; }
  .card--back .wordmark__firm { font-size: 36px; letter-spacing: .5px; }
  .card--back .wordmark__kind { font-size: 15px; letter-spacing: 3.6px; margin-top: 5px; }

  .card--back .faint-pattern { left: 0; top: 190px; width: 236px; height: 210px; opacity: .8; }

  .person { position: absolute; left: 384px; top: 70px; }
  .person__name { font-size: 25px; font-weight: 600; color: var(--navy); }
  .person__title { font-size: 15px; color: var(--text-grey); margin-top: 4px; }

  .contact { position: absolute; left: 384px; top: 194px; list-style: none; color: var(--navy); font-size: 16.5px; }
  .contact li { display: flex; align-items: center; height: 25px; }
  .contact svg { width: 16px; height: 16px; margin-right: 17px; fill: var(--grey); }
  .address { position: absolute; left: 384px; top: 281px; color: var(--navy); font-size: 16.5px; line-height: 24px; }

  .band { position: absolute; left: 0; bottom: 0; width: 712px; height: 20px; }
</style>
</head>
<body>
  <section class="card card--front">
    <div class="faint-pattern" role="img" aria-label="Faint repeated brand pattern"></div>
    <div class="logo-clear"></div>
    <div class="wordmark">
      <div class="wordmark__square"></div>
      <div class="wordmark__name">
        <span class="wordmark__firm">PELLMORE</span>
        <span class="wordmark__kind">ARCHITECTURE</span>
      </div>
    </div>
  </section>

  <section class="card card--back">
    <div class="wordmark">
      <div class="wordmark__square"></div>
      <div class="wordmark__name">
        <span class="wordmark__firm">PELLMORE</span>
        <span class="wordmark__kind">ARCHITECTURE</span>
      </div>
    </div>
    <div class="faint-pattern" role="img" aria-label="Large faint brand decoration"></div>

    <div class="person">
      <p class="person__name">Your name</p>
      <p class="person__title">Your Title</p>
    </div>

    <ul class="contact">
      <li><svg viewBox="0 0 16 16"><path d="M2 5c0-2 3-3 6-3s6 1 6 3v1h-3V5H5v1H2zM4 7h8l2 6H2zM8 8.5a2 2 0 1 0 0 4a2 2 0 1 0 0-4z"/></svg>+00 111 222 3333</li>
      <li><svg viewBox="0 0 16 16"><path d="M1 3h14v10H1zM2.5 4.5v.6L8 9l5.5-3.9v-.6zM2.5 6.8v4.7h11V6.8L8 10.7z"/></svg>yourname@yourwebsite.com</li>
      <li><svg viewBox="0 0 16 16"><path d="M8 1a7 7 0 1 0 0 14A7 7 0 0 0 8 1zm-1 1.6C5.8 4 5.2 5.6 5.1 7.3H2.6A5.5 5.5 0 0 1 7 2.6zm2 0a5.5 5.5 0 0 1 4.4 4.7h-2.5C10.8 5.6 10.2 4 9 2.6zM7.5 2.9c.9 1.2 1.5 2.7 1.6 4.4H6.4c.1-1.7.6-3.2 1.1-4.4zM2.6 8.7h2.5c.1 1.7.7 3.3 1.9 4.7a5.5 5.5 0 0 1-4.4-4.7zm3.8 0h2.7c-.1 1.7-.7 3.2-1.6 4.4-.6-1.2-1-2.7-1.1-4.4zm4.5 0h2.5A5.5 5.5 0 0 1 9 13.4c1.2-1.4 1.8-3 1.9-4.7z"/></svg>www.yourwebsite.com</li>
    </ul>

    <p class="address">Your Long Commercial or business<br>address in just two line.</p>

    <svg class="band" viewBox="0 0 712 20" preserveAspectRatio="none" aria-hidden="true">
      <rect x="0" y="0" width="712" height="20" fill="#a3a3a3"/>
      <polygon points="0,0 500,0 468,20 0,20" fill="#2b4a70"/>
      <polygon points="500,0 508,0 476,20 468,20" fill="#ffffff"/>
    </svg>
  </section>
</body>
</html>
```